依頼概要
■ 依頼の目的/概要
旅館の焼酎・清酒のプライベートラベルです。
旅館のイメージはHPにて確認ください。
http://www.kogetsuen-ryokan.example/

■ 重視する点/検討基準
10cm×10cmでお願いします。

■ 利用用途
納品ファイルはイラストレーター形式希望

■ その他/注意点
御客様の依頼としては、メインで「月波荘」が乗っていてほしいようです。
ご提案有難うございます。
旅館の方より、旅館のイメージ色の緑を基調にしたいとの依頼を頂きました。
お手数をおかけいたしますが
よろしくおねがいいたします。
依頼期間の延長をさせてください。
商品の瓶です。
麦 900ml
芋 720ml
■ 選んだ理由

当初、グリーンを基調にということだったのですが、
月波荘のロゴがバックに薄く入っている所が気に入られたようです。

■ 提案者全員のお礼・コメント

たくさん参加して頂き有難うござました。
使用する絵はお客様が決められますが、ほんとにいいものばかりでした。
また、是非ご参加して頂きます様お願い致します。
ほんとに有難うござました。

```html
<!DOCTYPE html>
<html lang="ja">
<head>
<meta charset="utf-8">
<title>月波荘 清酒ラベル</title>
<link href="https://fonts.googleapis.com/css2?family=Shippori+Mincho:wght@500;700&display=swap" rel="stylesheet">
<style>
  :root {
    --page: #ffffff;
    --leaf-light: #a9c247;
    --leaf-mid: #8caa30;
    --rule: #5d7a1b;
    --name-fill: #ffffff;
    --accent-red: #c8141c;
    --ink: #2f4410;
  }
  * { margin: 0; padding: 0; box-sizing: border-box; }
  html, body {
    width: 895px; height: 1200px; overflow: hidden;
    background: var(--page);
  }
  .canvas {
    position: relative; width: 895px; height: 1200px;
    display: flex; align-items: center; justify-content: center;
  }
  .label {
    position: relative; width: 640px; height: 1100px; overflow: hidden;
    border-top: 5px solid var(--rule);
    border-bottom: 5px solid var(--rule);
  }
  .label-texture {
    position: absolute; inset: 0;
    background: linear-gradient(90deg, var(--leaf-mid) 0%, var(--leaf-light) 35%, var(--leaf-light) 65%, var(--leaf-mid) 100%);
  }
  .label-content { position: relative; height: 100%; font-family: "Shippori Mincho", serif; }
  .top-line {
    position: absolute; top: 36px; left: 0; right: 0; text-align: center;
    font-size: 20px; font-weight: 500; letter-spacing: 6px; color: var(--ink);
  }
  .top-rule {
    position: absolute; top: 76px; left: 50px; right: 50px;
    height: 2px; background: var(--rule);
  }
  .grade {
    position: absolute; top: 120px; right: 90px;
    writing-mode: vertical-rl;
    font-weight: 700; font-size: 36px; letter-spacing: 6px;
    color: var(--accent-red);
  }
  .brand-name {
    position: absolute; top: 170px; left: 50%; transform: translateX(-50%);
    writing-mode: vertical-rl;
    font-weight: 700; font-size: 210px; line-height: 1; letter-spacing: 20px;
    color: var(--name-fill);
  }
  .maker-line {
    position: absolute; bottom: 110px; left: 0; right: 0; text-align: center;
    font-size: 20px; font-weight: 500; letter-spacing: 6px; color: var(--ink);
  }
  .maker {
    position: absolute; bottom: 44px; left: 0; right: 0;
    display: flex; align-items: center; justify-content: center; gap: 14px;
    font-weight: 700; font-size: 38px; color: var(--ink);
  }
  .maker-mark {
    width: 30px; height: 30px; border-radius: 50%;
    border: 4px solid var(--ink);
  }
</style>
</head>
<body>
  <main class="canvas">
    <section class="label">
      <div class="label-texture" role="img" aria-label="緑の竹の模様の背景"></div>
      <div class="label-content">
        <p class="top-line">旅館月波荘 謹製 特別限定酒</p>
        <div class="top-rule"></div>
        <p class="grade">清酒大吟醸</p>
        <h1 class="brand-name">月波荘</h1>
        <p class="maker-line">湯の宿 謹製</p>
        <div class="maker"><span class="maker-mark"></span><span>月波荘</span></div>
      </div>
    </section>
  </main>
</body>
</html>
```